Online Jewellery Marketing Design Project

I need a simple colour business card with a style that can easily be transferred into grayscale and can be used for as part of the design for brochures and gift certificates.

Design to revolve around Script, Peacock feathers and the colours found in them. I would also be open to a rich purple.

The business is a small discount online jewellery and painting sales. As business improves the designs will need to be able to be used on the card backings of the jewellery, a website with cart capability and other marketing tools.

The final design should communicate inexpensive style.

I have include some of the designs I have been using while this was just a hobby. Now that it is moving towards a proper business, even if only part time, a more professional touch is required.

Industry/Entity Type

Marketing

Logo Text

Mabel's Trinket Jewellery & Paintings

```html
<!DOCTYPE html>
<html lang="en">
<head>
<meta charset="utf-8">
<title>Mabel's Trinket – Business Card</title>
<link href="https://fonts.googleapis.com/css2?family=Great+Vibes&family=Dancing+Script:wght@400&display=swap" rel="stylesheet">
<style>
  :root {
    --backdrop: #2a2a2c;
    --card-black: #0b0b0c;
    --curve-white: #f2f2f2;
    --text-light: #e9e9e9;
    --feather-teal: #1f7d86;
    --feather-blue: #1c2f8a;
    --feather-green: #4e6a2a;
    --feather-bronze: #5a4a22;
    --badge-orange: #d0551f;
    --badge-blue: #3b5ea8;
  }
  * { margin: 0; padding: 0; box-sizing: border-box; }
  html, body {
    width: 1200px; height: 900px; overflow: hidden;
    background: var(--backdrop);
  }
  .business-card {
    position: absolute;
    left: 150px; top: 193px;
    width: 900px; height: 514px;
    background: var(--card-black);
    box-shadow: 0 18px 40px rgba(0,0,0,.55);
    overflow: hidden;
  }
  .card-shapes { position: absolute; inset: 0; }
  .brand {
    position: absolute; left: 0; right: 0; top: 70px;
    text-align: center; color: var(--text-light);
    font-family: "Great Vibes", cursive;
  }
  .brand-name { font-size: 64px; line-height: 1; }
  .brand-tagline { font-size: 36px; line-height: 1.1; margin-top: 2px; }
  .contact {
    position: absolute; left: 0; right: 0; top: 238px;
    text-align: center; color: var(--text-light);
    font-family: "Dancing Script", cursive;
  }
  .contact-line { font-size: 30px; line-height: 1.35; }
  .social { margin-top: 14px; display: inline-block; text-align: left; }
  .social-line { font-size: 25px; line-height: 1.35; display: flex; align-items: center; gap: 12px; }
  .badge-square { width: 22px; height: 14px; background: var(--badge-orange); }
  .badge-circle { width: 14px; height: 14px; border-radius: 50%; background: var(--badge-blue); margin: 0 4px; }
</style>
</head>
<body>
  <div class="business-card">
    <svg class="card-shapes" width="900" height="514" viewBox="0 0 900 514">
      <defs>
        <radialGradient id="featherTones" cx="50%" cy="50%" r="70%">
          <stop offset="0%" stop-color="var(--feather-blue)"/>
          <stop offset="35%" stop-color="var(--feather-teal)"/>
          <stop offset="65%" stop-color="var(--feather-green)"/>
          <stop offset="100%" stop-color="var(--feather-bronze)"/>
        </radialGradient>
      </defs>
      <path class="feather-panel-left" role="img" aria-label="Peacock feather photograph with blue and teal eyes"
            d="M0,110 C80,100 165,140 172,235 C180,335 120,420 200,514 H0 Z"
            fill="url(#featherTones)"/>
      <path class="curve-left" d="M0,110 C80,100 165,140 172,235 C180,335 120,420 200,514"
            fill="none" stroke="var(--curve-white)" stroke-width="7"/>
      <path class="feather-panel-right" role="img" aria-label="Peacock feather photograph with blue and teal eyes"
            d="M770,0 C720,60 705,150 745,225 C790,305 770,420 690,514 H900 V0 Z"
            fill="url(#featherTones)"/>
      <path class="curve-right" d="M770,0 C720,60 705,150 745,225 C790,305 770,420 690,514"
            fill="none" stroke="var(--curve-white)" stroke-width="7"/>
    </svg>

    <div class="brand">
      <div class="brand-name">Mabel's Trinket</div>
      <div class="brand-tagline">Jewellery &amp; Paintings</div>
    </div>

    <div class="contact">
      <div class="contact-line">MabelsTrinket@mailbox.com</div>
      <div class="contact-line">stores.auctionhub.com.au/trinketlady/</div>
      <div class="social">
        <div class="social-line"><span class="badge-square"></span>www.craftmarket.com/shop/MabelsTrinket</div>
        <div class="social-line"><span class="badge-circle"></span>www.friendspace.com/MabelsTrinket</div>
      </div>
    </div>
  </div>
</body>
</html>
```